Stonebay Towing Business Card

Towing
Accident towing
Mechanical breakdown
Insurance, salvage and recovery
4wd off road towing
Light & Heavy towing
8347 2516
24 hour business 7 days

Logo can be whole size on front

Industry/Entity Type

Towing/ transport

Contact Information for Business Card

The above

```html
<!DOCTYPE html>
<html lang="en">
<head>
<meta charset="utf-8">
<title>Stonebay Towing – Business Card</title>
<link href="https://fonts.googleapis.com/css2?family=Tenor+Sans&family=Lato:wght@700;900&display=swap" rel="stylesheet">
<style>
  :root {
    --page-bg: #d9d4ce;
    --ink: #1e1c1c;
    --black: #0d0d0d;
    --red: #b3151c;
    --red-dark: #7d0c10;
    --silver-light: #f1efed;
    --silver-mid: #d6d1cc;
    --silver-dark: #a9a39e;
  }
  * { margin: 0; padding: 0; box-sizing: border-box; }
  html, body {
    width: 1200px; height: 970px; overflow: hidden;
    background: var(--page-bg);
  }
  .business-card {
    position: absolute;
    left: 50px; top: 171px;
    width: 1180px; height: 674px;
    transform: scale(0.932);
    transform-origin: top left;
    overflow: hidden;
    box-shadow: 0 18px 40px rgba(0,0,0,0.25);
    font-family: "Tenor Sans", sans-serif;
    color: var(--ink);
  }
  .card-background { position: absolute; inset: 0; width: 100%; height: 100%; }
  .brand-name {
    position: absolute;
    left: 690px; top: 100px; width: 460px;
    text-align: center;
    font-family: "Tenor Sans", sans-serif;
    font-size: 50px;
    color: var(--red);
    letter-spacing: 1px;
  }
  .services-title {
    position: absolute; left: 70px; top: 218px;
    font-family: "Lato", sans-serif; font-weight: 700;
    font-size: 33px; color: var(--red); letter-spacing: 1px;
  }
  .services-list {
    position: absolute; left: 72px; top: 294px;
    list-style: none;
  }
  .services-list li {
    position: relative;
    padding-left: 37px;
    font-size: 26px;
    line-height: 42.3px;
    letter-spacing: 0.3px;
    color: var(--ink);
  }
  .services-list li::before {
    content: "";
    position: absolute; left: 0; top: 13px;
    width: 17px; height: 17px; border-radius: 50%;
    background: var(--red);
  }
  .hours {
    position: absolute; left: 72px; top: 574px;
    font-family: "Lato", sans-serif; font-weight: 700;
    font-size: 30px; letter-spacing: 0.8px; color: var(--ink);
  }
  .hours .accent { color: var(--red); }
  .phone {
    position: absolute; left: 880px; top: 572px;
    display: flex; align-items: center; gap: 12px;
    font-family: "Lato", sans-serif; font-weight: 900;
    font-size: 31px; color: var(--black); letter-spacing: 0.5px;
  }
  .phone-icon { width: 42px; height: 42px; }
</style>
</head>
<body>
  <div class="business-card">
    <svg class="card-background" viewBox="0 0 1180 674" preserveAspectRatio="none" aria-hidden="true">
      <defs>
        <linearGradient id="silverFace" x1="0" y1="0" x2="1" y2="1">
          <stop offset="0" stop-color="var(--silver-light)"/>
          <stop offset="0.5" stop-color="var(--silver-mid)"/>
          <stop offset="1" stop-color="#c9c3bd"/>
        </linearGradient>
        <linearGradient id="redBand" x1="0" y1="0" x2="1" y2="0">
          <stop offset="0" stop-color="var(--red)"/>
          <stop offset="0.6" stop-color="var(--red-dark)"/>
          <stop offset="1" stop-color="var(--red)"/>
        </linearGradient>
      </defs>
      <rect class="silver-face" width="1180" height="674" fill="url(#silverFace)"/>
      <path class="grey-wave" d="M0 175 C300 120 480 150 650 250 C850 365 1000 450 1180 400 V450 C1000 490 850 420 650 290 C480 190 300 160 0 200 Z" fill="var(--silver-dark)" opacity="0.55"/>
      <path class="red-wave" d="M0 150 C300 100 480 125 650 225 C850 345 1000 420 1180 330 V418 C1000 455 850 395 650 265 C480 165 300 140 0 172 Z" fill="url(#redBand)"/>
      <path class="black-field" d="M0 0 H1180 V330 C1000 395 850 330 650 222 C480 122 300 100 0 150 Z" fill="var(--black)"/>
    </svg>

    <div class="brand-name">Stonebay Towing</div>

    <h2 class="services-title">OUR SERVICES</h2>
    <ul class="services-list">
      <li>TOWING</li>
      <li>ACCIDENT TOWING</li>
      <li>MECHANICAL BREAKDOWN</li>
      <li>INSURANCE, SALVAGE AND RECOVERY</li>
      <li>4WD OFF ROAD TOWING</li>
      <li>LIGHT &amp; HEAVY TOWING</li>
    </ul>

    <p class="hours"><span class="accent">24 HOUR</span> BUSINESS <span class="accent">7 DAYS</span></p>

    <div class="phone">
      <svg class="phone-icon" viewBox="0 0 42 42" aria-hidden="true">
        <circle cx="21" cy="21" r="21" fill="var(--red)"/>
        <path d="M15 11 l4 0 l2 6 l-3 2 c1 3 3 5 6 6 l2 -3 l6 2 l0 4 c0 1 -1 2 -2 2 c-9 0 -17 -8 -17 -17 c0 -1 1 -2 2 -2 z" fill="#fff"/>
      </svg>
      <span class="phone-number">8347 2516</span>
    </div>
  </div>
</body>
</html>
```